Q7M Electrical Systems Inc Business Cards

Target Market(s)

Customers

Industry/Entity Type

Construction - Electrical

Contact Information for Business Card

Company Name, Address, Phone, and email address

Font styles to use
Sans Serif

Colors
0054AA
0677BA
7BADD7
CADEEF
E8F1F8

Requirements
Must have
• we would like to use the same design that we had our vehicles wrapped
Nice to have
• The design that we used on our trucks

```html
<!DOCTYPE html>
<html lang="en">
<head>
<meta charset="UTF-8">
<title>Q7M Electrical Systems Inc Business Cards</title>
<link rel="stylesheet" href="https://fonts.googleapis.com/css2?family=Poppins:wght@400;600&display=swap">
<style>
  :root {
    --bg: #2b2b2d;
    --navy: #0b1448;
    --navy-deep: #071038;
    --blue-bright: #1f4fd8;
    --white: #ffffff;
  }
  html, body {
    margin: 0;
    padding: 0;
    width: 1200px;
    height: 1108px;
    overflow: hidden;
    background: var(--bg);
    font-family: "Poppins", sans-serif;
  }
  .stage {
    position: relative;
    width: 1200px;
    height: 1108px;
  }
  .card {
    position: absolute;
    top: 184px;
    width: 440px;
    height: 740px;
    border-radius: 28px;
    overflow: hidden;
    box-shadow: 0 18px 40px rgba(0,0,0,0.45);
  }
  .card-front {
    left: 130px;
    background: var(--white);
  }
  .card-back {
    left: 630px;
    background: var(--navy);
  }
  .front-waves {
    position: absolute;
    inset: 0;
    width: 440px;
    height: 740px;
  }
  .brand-name {
    position: absolute;
    top: 120px;
    left: 40px;
    right: 40px;
    text-align: center;
    color: var(--navy);
    font-weight: 600;
    font-size: 34px;
    line-height: 1.2;
  }
  .brand-rule {
    position: absolute;
    top: 258px;
    left: 90px;
    width: 260px;
    height: 2px;
    background: var(--navy);
  }
  .contact {
    position: absolute;
    left: 0;
    right: 0;
    top: 540px;
    text-align: center;
    color: var(--white);
    font-size: 19px;
    line-height: 1.45;
  }
  .contact p { margin: 0; }
  .contact-divider {
    width: 64px;
    height: 1px;
    background: var(--white);
    margin: 16px auto;
  }
  .back-pattern {
    position: absolute;
    inset: 0;
    background:
      radial-gradient(ellipse at 85% 10%, rgba(31,79,216,0.75), rgba(31,79,216,0) 60%),
      linear-gradient(160deg, var(--navy) 0%, var(--navy-deep) 100%);
  }
  .back-name {
    position: absolute;
    left: 0;
    right: 0;
    top: 470px;
    text-align: center;
    color: var(--white);
    font-weight: 600;
    font-size: 20px;
  }
</style>
</head>
<body>
<main class="stage">
  <section class="card card-front">
    <svg class="front-waves" viewBox="0 0 440 740" aria-hidden="true">
      <path d="M0 320 C150 395 300 440 440 452 L440 462 C290 458 140 425 0 362 Z" fill="var(--navy)"/>
      <path d="M0 392 C150 445 300 472 440 478 L440 740 L0 740 Z" fill="var(--navy)"/>
      <path d="M50 398 C170 450 310 478 440 486" fill="none" stroke="var(--white)" stroke-width="4"/>
      <path d="M90 404 C200 452 320 480 440 496" fill="none" stroke="var(--white)" stroke-width="6"/>
    </svg>
    <div class="brand-name">Q7M Electrical Systems Inc</div>
    <div class="brand-rule"></div>
    <div class="contact">
      <p>482 Harbor Ridge Way # 210</p>
      <p>Lakewood Springs, FL 32790</p>
      <div class="contact-divider"></div>
      <p>407-555-0182</p>
      <p>info@q7melectric.com</p>
    </div>
  </section>
  <section class="card card-back">
    <div class="back-pattern" role="img" aria-label="Repeating brand mark pattern in glossy blue on navy"></div>
    <div class="back-name">Q7M Electrical Systems Inc</div>
  </section>
</main>
</body>
</html>
```